Luxury Brand Real Estate For Sale sign

**Update** I've added some examples from the internet of other signs that have a look similar to what I would like to see. I do not want my personal name in the sign. And the word FOR SALE Does not need to be so large - it can be more subtle.
I want to create a Real Estate for sale sign for my company that will be used for luxury/higher end real estate listings. I’m sharing my business card as well as a logo with new teal color to show what we're moving towards: we’re using Teal, white, black and gold.
Hoping the sign is simple, sophisticated and eye catching.
The sign should be 24" wide by 30" tall including the company name: Harbor Crest Realty Group and our logo, office phone number 727-555-0148 and website www.hcrgexample.com the words "For Sale"
Optional to add this e-mail address info@hcrgexample.com to the sign
Target Market(s)
Luxury home buyers
Industry/Entity Type
Real Estate
Look and feel

```html
<!DOCTYPE html>
<html lang="en">
<head>
<meta charset="utf-8">
<title>Harbor Crest Realty Group – For Sale Sign</title>
<link rel="stylesheet" href="https://fonts.googleapis.com/css2?family=Alegreya:wght@800&family=Josefin+Sans:wght@300;400&family=Poppins:wght@400;700&display=swap">
<style>
  :root {
    --teal: #07807f;
    --gold: #d9a93a;
    --gold-light: #f1d27a;
    --ink: #1c1c1c;
    --white: #ffffff;
    --mist: #e8eeee;
    --backdrop: #f2f2f0;
  }
  html, body {
    margin: 0;
    width: 1190px;
    height: 1200px;
    overflow: hidden;
    background: var(--backdrop);
  }
  .sign {
    position: absolute;
    left: 170px;
    top: 35px;
    width: 850px;
    height: 1130px;
    box-shadow: 0 6px 24px rgba(0,0,0,0.12);
  }
  .sign svg { display: block; }
  .brand-mark { font-family: "Josefin Sans", sans-serif; font-weight: 400; fill: var(--teal); }
  .brand-name { font-family: "Josefin Sans", sans-serif; font-weight: 300; fill: var(--teal); }
  .brand-sub { font-family: "Josefin Sans", sans-serif; font-weight: 300; fill: var(--ink); letter-spacing: 11px; }
  .headline { font-family: "Alegreya", serif; font-weight: 800; fill: var(--white); }
  .phone { font-family: "Poppins", sans-serif; font-weight: 700; fill: var(--teal); }
  .website { font-family: "Poppins", sans-serif; font-weight: 400; fill: var(--ink); letter-spacing: 6px; }
</style>
</head>
<body>
<div class="sign">
  <svg width="850" height="1130" viewBox="0 0 850 1130" xmlns="http://www.w3.org/2000/svg">
    <defs>
      <linearGradient id="panelTone" x1="0" y1="0" x2="1" y2="1">
        <stop offset="0" stop-color="var(--white)"/>
        <stop offset="1" stop-color="var(--mist)"/>
      </linearGradient>
      <linearGradient id="goldTone" x1="0" y1="0" x2="1" y2="0">
        <stop offset="0" stop-color="var(--gold)"/>
        <stop offset="0.5" stop-color="var(--gold-light)"/>
        <stop offset="1" stop-color="var(--gold)"/>
      </linearGradient>
      <clipPath id="panelClip"><rect width="850" height="1130"/></clipPath>
    </defs>

    <rect class="panel" width="850" height="1130" fill="url(#panelTone)"/>

    <g class="brand-lockup">
      <rect x="78" y="92" width="14" height="14" fill="var(--teal)"/>
      <text class="brand-mark" x="104" y="170" font-size="58">HCRG</text>
      <line x1="300" y1="52" x2="300" y2="240" stroke="var(--ink)" stroke-width="3"/>
      <text class="brand-name" x="335" y="140" font-size="40">HARBOR CREST</text>
      <text class="brand-sub" x="335" y="176" font-size="24">REALTY GROUP</text>
    </g>

    <g class="headline-band" clip-path="url(#panelClip)">
      <ellipse cx="425" cy="560" rx="610" ry="292" fill="url(#goldTone)"/>
      <ellipse cx="425" cy="560" rx="610" ry="280" fill="var(--teal)"/>
      <text class="headline" x="425" y="540" font-size="250" text-anchor="middle">FOR</text>
      <text class="headline" x="425" y="765" font-size="265" text-anchor="middle">SALE</text>
    </g>

    <g class="contact">
      <circle cx="118" cy="955" r="36" fill="var(--teal)"/>
      <path d="M104 937c3-2 6-1 7 2l4 8c1 2 0 4-2 5l-3 2c2 5 6 9 11 11l2-3c1-2 3-3 5-2l8 4c3 1 4 4 2 7l-3 4c-3 3-8 4-13 2-11-5-20-14-25-25-2-5-1-10 2-13z" fill="var(--white)"/>
      <path d="M122 933a18 18 0 0 1 17 17M121 941a10 10 0 0 1 10 10" stroke="var(--white)" stroke-width="3.5" fill="none" stroke-linecap="round"/>
      <text class="phone" x="168" y="990" font-size="94" textLength="600" lengthAdjust="spacingAndGlyphs">727-555-0148</text>
      <text class="website" x="80" y="1075" font-size="56" textLength="680" lengthAdjust="spacingAndGlyphs">www.hcrgexample.com</text>
    </g>
  </svg>
</div>
</body>
</html>
```